KB Rubbish Removal Business Card

Hey,
I need a double sided business card designed for a rubbish removal business based in Australia. Logo is already chosen, similar colours preferred for both sides of the business card.

Details to include:

Front:

KB Rubbish Removal
Darren Holloway
Managing Director
Mobile: 0471 902 146
Email: darren@kbrubbishremoval.com.au
Website: kbrubbishremoval.com.au

Rear:

How did we do?
kbrubbishremoval.com.au/review

```html
<!DOCTYPE html>
<html lang="en">
<head>
<meta charset="utf-8">
<title>KB Rubbish Removal – Business Card</title>
<link rel="stylesheet" href="https://fonts.googleapis.com/css2?family=Montserrat:wght@600;700&family=Roboto:wght@400&display=swap">
<style>
  :root {
    --page-bg: #1b1b1b;
    --green-deep: #036b12;
    --green-mid: #0b8a23;
    --green-bright: #22b443;
    --green-text: #0d7a1e;
    --green-light-text: #1fae3c;
    --ink-soft: #3d3d3d;
    --white: #ffffff;
  }
  * { box-sizing: border-box; margin: 0; padding: 0; }
  html, body { width: 1200px; height: 900px; overflow: hidden; }
  body {
    background: var(--page-bg);
    display: flex;
    flex-direction: column;
    align-items: center;
    justify-content: center;
    gap: 40px;
    font-family: "Roboto", Arial, sans-serif;
  }
  .card {
    width: 620px;
    height: 379px;
    position: relative;
    overflow: hidden;
    box-shadow: 0 10px 30px rgba(0,0,0,.55);
  }

  /* Rear side */
  .card-rear {
    background: linear-gradient(170deg, var(--green-deep) 0%, var(--green-mid) 45%, var(--green-bright) 100%);
    color: var(--white);
    display: flex;
    flex-direction: column;
    align-items: center;
    justify-content: center;
    text-align: center;
  }
  .rear-mark {
    width: 110px;
    height: 110px;
    border-radius: 50%;
    background: var(--green-bright);
    margin-bottom: 18px;
  }
  .rear-heading {
    font-family: "Montserrat", Arial, sans-serif;
    font-weight: 700;
    font-size: 30px;
    letter-spacing: .3px;
  }
  .rear-url {
    font-size: 14px;
    margin-top: 6px;
  }

  /* Front side */
  .card-front { background: var(--white); }
  .front-band {
    position: absolute;
    left: 0; right: 0; bottom: 0;
    height: 9px;
    background: linear-gradient(90deg, var(--green-deep), var(--green-bright));
  }
  .brand {
    position: absolute;
    top: 62px;
    right: 46px;
    display: flex;
    align-items: center;
    gap: 14px;
  }
  .brand-dot {
    width: 62px;
    height: 62px;
    border-radius: 50%;
    background: var(--green-light-text);
  }
  .brand-name {
    font-family: "Montserrat", Arial, sans-serif;
    font-weight: 700;
    font-size: 22px;
    line-height: 1.1;
    color: var(--green-text);
  }
  .person {
    position: absolute;
    left: 34px;
    bottom: 66px;
  }
  .person-name {
    font-family: "Montserrat", Arial, sans-serif;
    font-weight: 700;
    font-size: 24px;
    color: var(--green-text);
  }
  .person-role {
    font-size: 15px;
    color: var(--green-light-text);
    margin-top: 2px;
  }
  .contacts {
    position: absolute;
    right: 40px;
    bottom: 32px;
    list-style: none;
    display: flex;
    flex-direction: column;
    gap: 6px;
  }
  .contact {
    display: flex;
    align-items: center;
    justify-content: flex-end;
    gap: 10px;
    font-size: 12.5px;
    color: var(--ink-soft);
  }
  .contact-icon {
    width: 22px;
    height: 22px;
    flex: none;
  }
</style>
</head>
<body>

  <section class="card card-rear" aria-label="Card rear">
    <div class="rear-mark"></div>
    <p class="rear-heading">How did we do?</p>
    <p class="rear-url">kbrubbishremoval.com.au/review</p>
  </section>

  <section class="card card-front" aria-label="Card front">
    <div class="brand">
      <div class="brand-dot"></div>
      <p class="brand-name">KB Rubbish<br>Removal</p>
    </div>

    <div class="person">
      <p class="person-name">Darren Holloway</p>
      <p class="person-role">Managing Director</p>
    </div>

    <ul class="contacts">
      <li class="contact">
        <span>0471 902 146</span>
        <svg class="contact-icon" viewBox="0 0 22 22" aria-hidden="true">
          <circle cx="11" cy="11" r="11" fill="#1fae3c"/>
          <rect x="7.5" y="5" width="7" height="12" rx="1.2" fill="none" stroke="#fff" stroke-width="1.5"/>
          <line x1="10" y1="15" x2="12" y2="15" stroke="#fff" stroke-width="1.2"/>
        </svg>
      </li>
      <li class="contact">
        <span>darren@kbrubbishremoval.com.au</span>
        <svg class="contact-icon" viewBox="0 0 22 22" aria-hidden="true">
          <circle cx="11" cy="11" r="11" fill="#1fae3c"/>
          <rect x="5.5" y="7" width="11" height="8" rx="1" fill="none" stroke="#fff" stroke-width="1.4"/>
          <polyline points="5.8,7.4 11,11.6 16.2,7.4" fill="none" stroke="#fff" stroke-width="1.4"/>
        </svg>
      </li>
      <li class="contact">
        <span>kbrubbishremoval.com.au</span>
        <svg class="contact-icon" viewBox="0 0 22 22" aria-hidden="true">
          <circle cx="11" cy="11" r="11" fill="#1fae3c"/>
          <circle cx="11" cy="11" r="6" fill="none" stroke="#fff" stroke-width="1.3"/>
          <ellipse cx="11" cy="11" rx="2.6" ry="6" fill="none" stroke="#fff" stroke-width="1.1"/>
          <line x1="5" y1="11" x2="17" y2="11" stroke="#fff" stroke-width="1.1"/>
        </svg>
      </li>
    </ul>

    <div class="front-band"></div>
  </section>

</body>
</html>
```